Wine Bottle Lable

Want a unique, simple but elegant, label for a wine bottle. I want to use the letters "TWG" in the design which is a moniker for my last name "Tallwidge". The letters TWG do not have to be juxtaposed together so that it is recognizable, or they could be something like T-WG, WG-T, TGW T-WG-T, etc. The X could be totally separated from the NO, or otherwise. The wine is a white wine in a clear bottle. I need Adobe Illustrator files so I can add the wine varietal, year, alcohol content. The label should be 4" wide and 5" tall.

Colors

Designer to choose colors to be used in the design.

Requirements
Nice to have
• outstanding but simple graphics

```html
<!DOCTYPE html>
<html lang="en">
<head>
<meta charset="UTF-8">
<title>Tallwidge T-WG White Wine Label</title>
<link rel="stylesheet" href="https://fonts.googleapis.com/css2?family=Cinzel:wght@400&family=Arimo:wght@400;700&family=Montserrat:wght@400;500&display=swap">
<style>
  :root {
    --page-bg: #ffffff;
    --label-edge: #3e5f63;
    --label-frame: #c9dad6;
    --label-top: #5c7d7c;
    --label-mid: #9fbcb7;
    --label-low: #b9d0cb;
    --text-light: #eef4f2;
    --text-soft: #d6e3e0;
    --text-dark: #24393c;
    --sea-deep: #1d3a48;
    --sea-mid: #3f6f73;
    --sky-pale: #c3d9d3;
  }
  * { margin: 0; padding: 0; box-sizing: border-box; }
  html, body {
    width: 1200px;
    height: 1200px;
    overflow: hidden;
    background: var(--page-bg);
  }
  .canvas {
    position: relative;
    width: 1200px;
    height: 1200px;
  }
  .wine-label {
    position: absolute;
    left: 240px;
    top: 150px;
    width: 720px;
    height: 900px;
  }
  .label-shape {
    position: absolute;
    inset: 0;
    width: 720px;
    height: 900px;
  }
  .label-content {
    position: absolute;
    inset: 0;
    text-align: center;
  }
  .wine-type {
    position: absolute;
    top: 92px;
    width: 100%;
    font-family: "Cinzel", serif;
    font-size: 30px;
    letter-spacing: 0.42em;
    color: var(--text-soft);
  }
  .winery-name {
    position: absolute;
    top: 190px;
    width: 100%;
    font-family: "Arimo", sans-serif;
    font-size: 40px;
    color: var(--text-dark);
    letter-spacing: 0.01em;
  }
  .brand-mark {
    position: absolute;
    top: 232px;
    width: 100%;
    font-family: "Montserrat", sans-serif;
    font-weight: 400;
    font-size: 124px;
    letter-spacing: 0.02em;
    color: var(--text-light);
    line-height: 1.1;
  }
  .vine-note {
    position: absolute;
    top: 374px;
    width: 100%;
    font-family: "Arimo", sans-serif;
    font-weight: 700;
    font-size: 13px;
    color: var(--text-dark);
  }
  .varietal {
    position: absolute;
    top: 392px;
    width: 100%;
    font-family: "Arimo", sans-serif;
    font-size: 27px;
    color: var(--text-dark);
  }
  .ship-scene {
    position: absolute;
    left: 22px;
    right: 22px;
    top: 440px;
    bottom: 22px;
    background: linear-gradient(180deg, rgba(195,217,211,0) 0%, var(--sky-pale) 35%, var(--sea-mid) 72%, var(--sea-deep) 100%);
    border-radius: 0 0 8px 8px;
  }
  .bottle-facts {
    position: absolute;
    left: 40px;
    top: 655px;
    text-align: left;
    font-family: "Arimo", sans-serif;
    font-size: 13px;
    line-height: 1.35;
    color: var(--text-dark);
  }
</style>
</head>
<body>
<main class="canvas">
  <section class="wine-label">
    <svg class="label-shape" viewBox="0 0 720 900" aria-hidden="true">
      <defs>
        <linearGradient id="labelFill" x1="0" y1="0" x2="0" y2="1">
          <stop offset="0" stop-color="var(--label-top)"/>
          <stop offset="0.45" stop-color="var(--label-mid)"/>
          <stop offset="1" stop-color="var(--label-low)"/>
        </linearGradient>
      </defs>
      <path class="label-edge" fill="var(--label-edge)"
        d="M40,0 H680 A40,40 0 0 0 720,40 V860 A40,40 0 0 0 680,900 H40 A40,40 0 0 0 0,860 V40 A40,40 0 0 0 40,0 Z"/>
      <path class="label-panel" fill="url(#labelFill)" stroke="var(--label-frame)" stroke-width="2"
        d="M46,12 H674 A34,34 0 0 0 708,46 V854 A34,34 0 0 0 674,888 H46 A34,34 0 0 0 12,854 V46 A34,34 0 0 0 46,12 Z"/>
    </svg>
    <div class="label-content">
      <p class="wine-type">WHITE WINE</p>
      <p class="winery-name">TALLWIDGE</p>
      <h1 class="brand-mark">T-WG</h1>
      <p class="vine-note">OLD VINE</p>
      <p class="varietal">CABERNET SAUVIGNON</p>
      <div class="ship-scene" role="img" aria-label="Illustration of a tall sailing ship on rough teal ocean waves"></div>
      <p class="bottle-facts">750ML<br>14.5% ALC/VOL</p>
    </div>
  </section>
</main>
</body>
</html>
```